Talbern Learning Recruitment Business Cards

We need business cards designed for our growing recruitment business.
We have just launched our offices in Sydney Melbourne and have a well established business in Perth. We are a fun young firm that specialise in Early Years Education Recruitment.
Our vision mission values are below
Our Vision:
To be:
the single, nationally recognised leader in the Early Childhood Sector.
a multifaceted organisation with a network of expertly driven facilities in the Early Childhood Sector, acknowledged as an organisation of integrity, innovation, heart and community.

Our Mission:
To provide superior quality recruitment services and solutions to the Early Childhood sector.
We empower our candidates to succeed.
We engage in trusted partnerships with our clients.
We grow our business/network/community, with passion and integrity.

Our Values:

We… are REAL
think: CUSTOMER
find: SOLUTIONS
achieve: RESULTS
enjoy: WHAT WE DO

Our website is www.talbernlearning.com feel free to visit it for inspiration.
Name Felix Ormsby
Title National Director
1300 057 812
0462 315 706
felix@talbernstaffing.com
website www.talbernlearning.com

I have attached our current business cards and logo designs to view

Target Market(s)

Recruitment

Industry/Entity Type

Business

Contact Information for Business Card

Name Felix Ormsby
Title National Director
1300 057 812
0462 315 706

Font styles to use
Serif

Requirements
Must have
• Company Values and the cities we have offices in Perth | Sydney | Melbourne
Nice to have
• Our Vision on the card
• Our Vision:
• To be a nationally recognised leader in the Early Childhood Sector.
• A multifaceted organisation with a network of expertly driven facilities in the Early Childhood Sector, acknowledged as an organisation of integrity, innovation, heart and community.

```html
<!DOCTYPE html>
<html lang="en">
<head>
<meta charset="utf-8">
<title>Talbern Learning Recruitment – Business Card</title>
<link href="https://fonts.googleapis.com/css2?family=Montserrat:wght@500;600;700&family=Open+Sans:wght@400;600;700&display=swap" rel="stylesheet">
<style>
  :root {
    --page-bg: #e9ecef;
    --card-bg: #f7f8f9;
    --brand-blue: #1d6fa5;
    --brand-blue-light: #3f95c8;
    --brand-blue-dark: #1a5d8d;
    --ink: #222a30;
    --white: #ffffff;
    --values-ink: rgba(255,255,255,0.34);
  }
  html, body {
    margin: 0;
    width: 1200px;
    height: 900px;
    overflow: hidden;
    background: var(--page-bg);
  }
  .business-card {
    position: absolute;
    left: 100px;
    top: 142px;
    width: 1000px;
    height: 616px;
    border-radius: 28px;
    background: var(--card-bg);
    overflow: hidden;
    box-shadow: 0 10px 30px rgba(0,0,0,0.12);
    font-family: "Open Sans", sans-serif;
    color: var(--ink);
  }
  .card-art { position: absolute; inset: 0; }
  .brand-mark {
    position: absolute;
    left: 54px;
    top: 77px;
    width: 176px;
    height: 176px;
    border-radius: 50%;
    border: 4px solid var(--brand-blue);
    box-sizing: border-box;
  }
  .brand-name {
    position: absolute;
    left: 248px;
    top: 124px;
    margin: 0;
    font-family: "Montserrat", sans-serif;
    font-weight: 600;
    font-size: 28px;
    line-height: 34px;
    letter-spacing: 1px;
    color: var(--brand-blue);
  }
  .brand-tagline {
    position: absolute;
    left: 54px;
    top: 256px;
    margin: 0;
    font-family: "Montserrat", sans-serif;
    font-weight: 600;
    font-size: 18px;
    color: var(--brand-blue);
  }
  .person-name {
    position: absolute;
    left: 54px;
    top: 345px;
    margin: 0;
    font-family: "Montserrat", sans-serif;
    font-weight: 600;
    font-size: 33px;
    color: var(--brand-blue);
  }
  .person-title {
    position: absolute;
    left: 54px;
    top: 392px;
    margin: 0;
    font-size: 23px;
  }
  .social-row {
    position: absolute;
    left: 54px;
    top: 524px;
    display: flex;
    align-items: center;
    gap: 14px;
    font-size: 23px;
  }
  .social-row .label { margin-right: 4px; }
  .social-tile {
    width: 36px;
    height: 36px;
    border-radius: 6px;
    background: var(--brand-blue-dark);
  }
  .contact-list {
    position: absolute;
    right: 42px;
    top: 162px;
    margin: 0;
    padding: 0;
    list-style: none;
    color: var(--white);
    font-weight: 600;
    font-size: 22px;
    text-align: right;
  }
  .contact-list li {
    display: flex;
    justify-content: flex-end;
    align-items: center;
    gap: 14px;
    height: 32px;
  }
  .contact-list svg { width: 20px; height: 20px; flex: none; }
  .company-values {
    position: absolute;
    left: 610px;
    top: 310px;
    margin: 0;
    padding: 0;
    list-style: none;
    color: var(--values-ink);
    font-weight: 700;
    font-size: 17px;
    line-height: 23px;
  }
  .company-values .value-lead { font-weight: 400; }
  .office-list {
    position: absolute;
    right: 62px;
    top: 432px;
    margin: 0;
    padding: 0;
    list-style: none;
    color: var(--white);
    font-family: "Montserrat", sans-serif;
    font-weight: 600;
    font-size: 30px;
    text-align: right;
  }
  .office-list li {
    display: flex;
    justify-content: flex-end;
    align-items: center;
    gap: 14px;
    height: 42px;
  }
  .office-list li::after {
    content: "";
    width: 11px;
    height: 11px;
    border-radius: 50%;
    background: var(--white);
  }
</style>
</head>
<body>
  <article class="business-card">
    <svg class="card-art" width="1000" height="616" viewBox="0 0 1000 616" aria-hidden="true">
      <defs>
        <linearGradient id="panelBlue" gradientUnits="userSpaceOnUse" x1="500" y1="0" x2="1000" y2="616">
          <stop offset="0" stop-color="#3f95c8"/>
          <stop offset="1" stop-color="#1a5d8d"/>
        </linearGradient>
      </defs>
      <path class="contact-panel" d="M662 0 A364 364 0 0 0 662 616 L1000 616 L1000 0 Z" fill="url(#panelBlue)"/>
    </svg>

    <div class="brand-mark"></div>
    <p class="brand-name">TALBERN<br>LEARNING</p>
    <p class="brand-tagline">Bringing quality to education recruitment</p>

    <h1 class="person-name">FELIX ORMSBY</h1>
    <p class="person-title">National Director</p>

    <div class="social-row">
      <span class="label">Find Us On:</span>
      <span class="social-tile"></span>
      <span class="social-tile"></span>
      <span class="social-tile"></span>
      <span class="social-tile"></span>
    </div>

    <ul class="contact-list">
      <li>1300 057 812
        <svg viewBox="0 0 20 20"><path d="M3 8c0-3 3-4 7-4s7 1 7 4l-3 1-1-2H7L6 9 3 8zM5 10h10l1 6H4z" fill="#fff"/></svg>
      </li>
      <li>0462 315 706
        <svg viewBox="0 0 20 20"><rect x="6" y="2" width="9" height="16" rx="1.5" fill="none" stroke="#fff" stroke-width="2"/><circle cx="10.5" cy="15" r="1" fill="#fff"/></svg>
      </li>
      <li>felix@talbernstaffing.com
        <svg viewBox="0 0 20 20"><rect x="3" y="5" width="14" height="10" fill="#fff"/><path d="M3 5l7 6 7-6" fill="none" stroke="#2a78ad" stroke-width="1.5"/></svg>
      </li>
      <li>www.talbernlearning.com
        <svg viewBox="0 0 20 20"><g fill="none" stroke="#fff" stroke-width="2" stroke-linecap="round"><path d="M9 11l-3 3a2.5 2.5 0 0 1-3.5-3.5l3-3"/><path d="M11 9l3-3a2.5 2.5 0 0 1 3.5 3.5l-3 3"/><path d="M8 12l4-4"/></g></svg>
      </li>
    </ul>

    <ul class="company-values" aria-label="Our values">
      <li><span class="value-lead">We… are</span> REAL</li>
      <li><span class="value-lead">think:</span> CUSTOMER</li>
      <li><span class="value-lead">find:</span> SOLUTIONS</li>
      <li><span class="value-lead">achieve:</span> RESULTS</li>
      <li><span class="value-lead">enjoy:</span> WHAT WE DO</li>
    </ul>

    <ul class="office-list">
      <li>Perth</li>
      <li>Sydney</li>
      <li>Melbourne</li>
    </ul>
  </article>
</body>
</html>
```